依頼詳細
学習塾の看板デザインをお願いします。
基板となるイメージはできていますので、
それをブラッシュアップしてもらいたいです。
写真が二種類あり、同じデザインで、写真を差し替えたバージョンを作ってください。
記載項目
会社名等 添付ファイル参照
サイズ 横1000縦1500
希望イメージ
シンプル 複雑
単色 カラフル
暗い 明るい
日常 高級
遊び心 厳粛
未来的 伝統的
女性的 男性的
希望する色
青系、水色系
納品ファイル
• イラストレーター形式 (.ai)
補足説明
ポイント

①習慣は才能を超える、というキャッチフレーズを中心に、スタイリッシュでおしゃれなんだけど、情熱が伝わってくるデザインに仕上げて欲しい。情熱は、細部へのこだわりで伝わってくるものと思っています。

②勉強は、将来のために、今できることを毎日コツコツ積み上げていく作業。
「習慣は才能を超える」という言葉は、それを実行していくためのマインドセット。
フリータイム個別指導というのは、それを支えるための仕組み。
一般の個別指導では、時間が限られていて、本人任せの部分が大きく、サポートしきれない。
ふゆもりは、それぞれの都合に合わせていつでも毎日でも通える。
小中高一貫指導で、やる気さえあれば、どこまでもフォローできるオンリーワンの塾。
そのことを、言葉ではなく、デザインで伝えられる看板にしたい。

③原案には、上記のような思いを込めているが、自分で表現できるものには限界を感じている。
プロの手を借りて、一歩先の、情熱のこもったデザインをお願いします。
追記
・シンプルだけど、細部にこだわり、丁寧に作りこまれているものを希望します。
設置場所の写真を添付しました。
これまでのご提案を見て

シンプルなもの2点
どちらかが良いなと考えています

これからご提案頂く方へ

よりシンプル、かつ
素人では作れない
他との差別化ができているデザイン
を希望します。
■ 選んだ理由

他との違いが明確だった。
自分では全くおもいつかないデザインだった。

■ 提案者全員のお礼・コメント

この度は、ご提案と修正等の迅速な対応、誠にありがとうございました。
デザインには大変満足しております。
また、何かあった時には、お願いしたいと思っています。

```html
<!DOCTYPE html>
<html lang="ja">
<head>
<meta charset="utf-8">
<title>学習塾ふゆもり 看板</title>
<link rel="stylesheet" href="https://fonts.googleapis.com/css2?family=Noto+Serif+JP:wght@400;500;600&family=Noto+Sans+JP:wght@500;700&display=swap">
<style>
  :root {
    --navy: #1d3f86;
    --band: #2350a0;
    --label: rgba(40, 86, 170, 0.9);
    --ink: #1b2f63;
    --grey: #5d6166;
    --tagline: #2c4c9c;
    --square: #8fb4d8;
    --white: #ffffff;
  }
  * { margin: 0; padding: 0; box-sizing: border-box; }
  html, body { width: 799px; height: 1200px; overflow: hidden; background: var(--white); }
  .sign {
    position: relative; width: 799px; height: 1200px; overflow: hidden;
    background: var(--white);
    font-family: "Noto Serif JP", serif;
  }
  .hero-photo {
    position: absolute; left: 0; top: 0; width: 799px; height: 641px;
    background:
      radial-gradient(ellipse at 72% 38%, #2a2f45 0%, #3b4260 22%, rgba(120,130,160,0.4) 45%, rgba(255,255,255,0) 65%),
      linear-gradient(180deg, #f4f6f8 0%, #e7ebef 60%, #d9dee5 100%);
  }
  .label-freetime {
    position: absolute; left: 37px; top: 340px; width: 358px; height: 50px;
    background: var(--label); color: var(--white);
    font-family: "Noto Sans JP", sans-serif; font-weight: 500;
    font-size: 34px; letter-spacing: 6px; line-height: 50px; text-align: center;
  }
  .label-course {
    position: absolute; left: 37px; top: 400px; width: 353px; height: 82px;
    background: var(--white); color: var(--ink);
    font-family: "Noto Sans JP", sans-serif; font-weight: 700;
    font-size: 56px; letter-spacing: 22px; line-height: 82px; text-align: center;
    padding-left: 22px;
  }
  .area-band {
    position: absolute; left: 0; top: 641px; width: 799px; height: 75px;
    background: var(--band); color: var(--white);
    font-size: 26px; line-height: 75px;
  }
  .area-band .grades { position: absolute; left: 190px; }
  .area-band .areas { position: absolute; left: 430px; letter-spacing: 2px; }
  .name-square {
    position: absolute; left: 140px; top: 872px; width: 104px; height: 104px;
    border: 4px solid var(--square);
  }
  .tagline {
    position: absolute; left: 290px; top: 842px; width: 440px;
    text-align center; text-align: center; color: var(--tagline);
    font-weight: 500; font-size: 34px; letter-spacing: 4px; line-height: 48px;
    white-space: nowrap;
  }
  .school-name {
    position: absolute; left: 290px; top: 898px; width: 440px;
    text-align: center; color: var(--grey);
    font-weight: 500; font-size: 66px; letter-spacing: 2px; line-height: 84px;
  }
  .school-sub {
    position: absolute; left: 290px; top: 988px; width: 440px;
    text-align: center; color: var(--grey);
    font-weight: 500; font-size: 28px; letter-spacing: 6px; line-height: 40px;
  }
  .contact-band {
    position: absolute; left: 0; top: 1117px; width: 799px; height: 83px;
    background: var(--navy); color: var(--white);
  }
  .contact-band .phone-icon { position: absolute; left: 40px; top: 24px; width: 36px; height: 36px; }
  .contact-band .phone {
    position: absolute; left: 84px; top: 0; line-height: 83px;
    font-family: "Noto Sans JP", sans-serif; font-weight: 500; font-size: 40px; letter-spacing: 1px;
  }
  .contact-band .access {
    position: absolute; right: 38px; top: 0; line-height: 83px;
    font-size: 28px; letter-spacing: 2px;
  }
</style>
</head>
<body>
<main class="sign">
  <div class="hero-photo" role="img" aria-label="制服姿の女子生徒が机に向かって勉強している写真"></div>
  <div class="label-freetime">フリータイム</div>
  <div class="label-course">個別指導</div>

  <div class="area-band">
    <span class="grades">小中高一貫</span>
    <span class="areas">東原 / 北山 / 南台</span>
  </div>

  <div class="name-square"></div>
  <p class="tagline">習慣は才能を超える</p>
  <p class="school-name">FUYUMORI</p>
  <p class="school-sub">学習塾ふゆもり</p>

  <div class="contact-band">
    <svg class="phone-icon" viewBox="0 0 24 24" aria-hidden="true">
      <path fill="#ffffff" d="M6.6 10.8a15.1 15.1 0 0 0 6.6 6.6l2.2-2.2a1 1 0 0 1 1-.25 11.4 11.4 0 0 0 3.6.57 1 1 0 0 1 1 1V20a1 1 0 0 1-1 1A17 17 0 0 1 3 4a1 1 0 0 1 1-1h3.5a1 1 0 0 1 1 1c0 1.25.2 2.450.57 3.57a1 1 0 0 1-.25 1z"/>
    </svg>
    <span class="phone">052-000-4817</span>
    <span class="access">桜丘駅３番出口すぐ</span>
  </div>
</main>
</body>
</html>
```